Business Card Design for a Lending Business (Hard Money loans)

We need a business card for our Real Estate Lending business. We do hard Money loans for real estate investors. We have an existing logo we like, see attached. I'd like the business card to mostly include the logo colors, but a bright color pop of some sort would be nice to see also. Card should include Logo, Company Name, Company Address, Employee Name, Cell Phone, Main Phone, Email, Website

Industry/Entity Type

Finance / Lending

Contact Information for Business Card

Logo, Company Name, Company Address, Employee Name, Cell Phone, Main Phone, Email, Website

Requirements
Nice to have
• I'd like the business card to mostly include the logo colors, but a bright color pop of some sort would be nice to see also.

```html
<!DOCTYPE html>
<html lang="en">
<head>
<meta charset="utf-8">
<title>Keystone Lending – Business Card</title>
<link href="https://fonts.googleapis.com/css2?family=Montserrat:wght@400;500;700&display=swap" rel="stylesheet">
<style>
  :root {
    --bg: #2b2b2d;
    --navy: #253a84;
    --blue-deep: #1c5fb0;
    --blue-mid: #3a8fd0;
    --blue-light: #56b3e6;
    --sky: #5fc0f0;
    --white: #ffffff;
    --ink: #1f2a4a;
  }
  * { box-sizing: border-box; margin: 0; padding: 0; }
  html, body { width: 1200px; height: 1186px; overflow: hidden; }
  body {
    background: var(--bg);
    font-family: "Montserrat", Arial, sans-serif;
    position: relative;
  }
  .card {
    position: absolute;
    left: 180px;
    width: 840px;
    height: 480px;
    border-radius: 26px;
    overflow: hidden;
    box-shadow: 0 14px 30px rgba(0,0,0,.45);
  }
  /* Back side */
  .card-back {
    top: 83px;
    background: linear-gradient(200deg, var(--blue-light) 0%, var(--blue-mid) 45%, var(--blue-deep) 100%);
    display: flex;
    align-items: center;
    justify-content: center;
  }
  .brand {
    display: flex;
    align-items: center;
    gap: 22px;
  }
  .brand-dot {
    width: 64px; height: 64px;
    border-radius: 50%;
    border: 10px solid currentColor;
    flex: none;
  }
  .brand-name {
    font-weight: 700;
    letter-spacing: 5px;
    line-height: 1.1;
    text-transform: uppercase;
  }
  .card-back .brand { color: var(--white); }
  .card-back .brand-name { font-size: 46px; }

  /* Front side */
  .card-front {
    top: 623px;
    background: var(--white);
  }
  .card-front svg.waves { position: absolute; inset: 0; }
  .person {
    position: absolute;
    left: 70px; top: 180px;
    color: var(--white);
  }
  .person-name { font-size: 27px; font-weight: 700; }
  .person-role { font-size: 16px; font-weight: 400; margin-top: 6px; padding-left: 24px; }
  .card-front .brand {
    position: absolute;
    right: 58px; top: 205px;
    color: var(--navy);
    gap: 14px;
  }
  .card-front .brand-dot { width: 44px; height: 44px; border-width: 7px; color: var(--blue-light); }
  .card-front .brand-name { font-size: 30px; letter-spacing: 3px; }
  .address {
    position: absolute;
    right: 58px; top: 295px;
    text-align: right;
    font-size: 15px;
    line-height: 1.45;
    color: var(--ink);
  }
  .contacts {
    position: absolute;
    left: 100px; top: 345px;
    list-style: none;
    font-size: 16px;
    color: var(--ink);
  }
  .contacts li { display: flex; align-items: center; gap: 12px; height: 26px; }
  .contacts svg { width: 15px; height: 15px; fill: var(--blue-mid); flex: none; }
</style>
</head>
<body>

<section class="card card-back" aria-label="Card back">
  <div class="brand">
    <span class="brand-dot"></span>
    <span class="brand-name">Keystone<br>Lending</span>
  </div>
</section>

<section class="card card-front" aria-label="Card front">
  <svg class="waves" viewBox="0 0 840 480" aria-hidden="true">
    <defs>
      <linearGradient id="blueField" x1="0" y1="1" x2="1" y2="0">
        <stop offset="0" stop-color="#5ab7e8"/>
        <stop offset="0.55" stop-color="#4aa4dc"/>
        <stop offset="1" stop-color="#2a62b0"/>
      </linearGradient>
    </defs>
    <path d="M0 0 H840 V50 C720 45 620 90 545 160 C470 235 380 320 0 322 Z" fill="var(--navy)"/>
    <path d="M470 215 C560 110 690 70 840 72" fill="none" stroke="var(--sky)" stroke-width="18"/>
    <path d="M0 0 H610 C550 60 510 160 430 232 C340 305 180 315 0 306 Z" fill="var(--white)"/>
    <path d="M0 0 H600 C540 58 500 155 420 226 C330 296 180 304 0 296 Z" fill="url(#blueField)"/>
  </svg>

  <div class="person">
    <p class="person-name">Daniel Mercer</p>
    <p class="person-role">CEO &amp; Founder</p>
  </div>

  <div class="brand">
    <span class="brand-dot"></span>
    <span class="brand-name">Keystone<br>Lending</span>
  </div>

  <p class="address">418 Harbor Point Rd<br>#112 Fairview, OH 43999</p>

  <ul class="contacts">
    <li><svg viewBox="0 0 16 16"><path d="M3 1h3l1.5 4-2 1.2a9 9 0 0 0 4.3 4.3L11 8.5l4 1.5v3a2 2 0 0 1-2 2C6.9 15 1 9.1 1 3a2 2 0 0 1 2-2z"/></svg>877-555-0142</li>
    <li><svg viewBox="0 0 16 16"><path d="M4 0h8a1 1 0 0 1 1 1v14a1 1 0 0 1-1 1H4a1 1 0 0 1-1-1V1a1 1 0 0 1 1-1zm1 2v10h6V2zm3 11a1 1 0 1 0 0 2 1 1 0 0 0 0-2z"/></svg>877-555-0142</li>
    <li><svg viewBox="0 0 16 16"><path d="M0 3h16v10H0zm1.5 1.2V5l6.5 4 6.5-4v-.8z"/></svg>info@keystonelending.com</li>
    <li><svg viewBox="0 0 16 16"><path d="M8 0a8 8 0 1 0 0 16A8 8 0 0 0 8 0zm0 1.5c.9 1 1.6 2.6 1.8 4.5H6.2C6.4 4.1 7.1 2.5 8 1.5zM1.6 7.5h3.1c0 1.6.4 3 .9 4.2A6.5 6.5 0 0 1 1.6 7.5zm4.6 0h3.6c-.1 2-.8 3.7-1.8 4.9-1-1.2-1.7-2.9-1.8-4.9zm5.1 0h3.1a6.5 6.5 0 0 1-4 4.2c.5-1.2.9-2.6.9-4.2z"/></svg>www.keystonelending.com</li>
  </ul>
</section>

</body>
</html>
```